The Quiet Harvest Book Cover

Cover for Multiauthor Ebook & Paper Print Book Cover

Book Title:
The Quiet Harvest: Field Notes Gathered By Many Guides for Thriving on Every Road Ahead

This book will offer the wisdom and philosophies of a variety of different coaches to allow future clients to get a taste of you and your style and prepare them to work with you!

A coach does not fix you. Or heal you. They coach you - offer thoughts to ponder, guidance, techniques to try. All to help you plays and succeed at the game of life.

Each coach has their own personality, training, experience, method and philosophy they bring to the table. The underlying purpose is to guide you through the quiet harvest, to become the person you desire and aspire to be. Different coaches for different folks, yet they all have their own unique wisdom and special sauce to share.

This book is a collection of just that. A tasting of the wisdom and philosophies of a variety of different coaches for you to experience.

Types of Coaches: Clarity, Dreams, Goals, Motivation, Mindset,  Subconscious, Beliefs, Behavior, Accountability, Life, Wellness, Love & Dating, Relationships, Sex, Business, Career,  Executive,  Personal Development,  Writing, Wellness, Fitness, Parenting,  Style, Spirituality, Public Speaking, Financial,  Time management, Weight Loss, Running, Self esteem,  Tarot, Astrology, Enneagram, Soul path/ Dharma, Skills, Performance,  Speaking / Communication, Leadership, Shadow Work, Acting, Sports, ANY & ALL

Target Market(s)

Males or females looking for guidance and words of wisdom from an expert coach - maybe to find one that resonates with them to work with further. Ages 16 and up. Any Gender. International. Looking to improve their life!

Industry/Entity Type

Self Development, Wellness, Coaching, Personal Growth, Fitness, Spirituality, Business, Relationships

Font styles to use
Serif
Script

Colors
0054AA
0677BA
7BADD7
CADEEF
E8F1F8
FFF300
FFF600
FEFA6F
FFFEC7
FFFEE8

Requirements
Must have
• I am looking for a visually appealing, unique cover that encompasses the breadth and depth of the transformation that people can go through and inspires them to want to grow and change even more. I love when elegant and classic simplicity is combined with some kind of twist that catches the eye and provokes thought. I love complimentary fonts, colors, design elements. You can visit my Bramblo Author Page - Dr. Marguerite Oslan Pardevy to see my titles to see what I have liked! But I am also excited to see where you can make my vision even better!!
Nice to have
• Front Cover - Image, Title and Subtitle, The Lantern Gate Publishing House, Spine - Title and Publishing House Logo, Back - Book Blurb, Authors Names, Info about Publishing House, ISBN Barcode
Should not have
• Anything too feminine or too masculine as I want to encourage coaches of all genders to participate.

```html
<!DOCTYPE html>
<html lang="en">
<head>
<meta charset="utf-8">
<title>The Quiet Harvest – Book Cover</title>
<link href="https://fonts.googleapis.com/css2?family=Cinzel:wght@400&family=Roboto:wght@400;500;700&family=Yellowtail&display=swap" rel="stylesheet">
<style>
  :root {
    --page-bg: #f1f1f1;
    --back-blue: #5f9ab5;
    --spine-blue: #79aec4;
    --front-white: #ffffff;
    --teal: #0d7a8c;
    --teal-deep: #0c6b7c;
    --pink: #d94a7c;
    --ink: #1d3340;
    --white: #ffffff;
    --photo-tone: #4e879f;
  }
  * { margin: 0; padding: 0; box-sizing: border-box; }
  html, body { width: 1200px; height: 900px; overflow: hidden; background: var(--page-bg); }
  .canvas { position: relative; width: 1200px; height: 900px; font-family: "Roboto", sans-serif; }

  .cover-panel { position: absolute; top: 137px; height: 648px; box-shadow: 0 2px 6px rgba(0,0,0,.18); }

  /* Back cover */
  .back-cover { left: 115px; width: 432px; background: var(--back-blue); color: var(--white); }
  .author-photo {
    position: absolute; left: 27px; top: 55px; width: 146px; height: 146px;
    border-radius: 50%; border: 3px solid var(--white);
    background: radial-gradient(circle at 50% 45%, #6fa3ba 0%, var(--photo-tone) 70%);
  }
  .bio-rule { position: absolute; left: 186px; top: 51px; width: 2px; height: 164px; background: var(--white); }
  .author-bio { position: absolute; left: 194px; top: 51px; width: 224px; font-size: 7.2px; line-height: 9.2px; }
  .about-heading { position: absolute; left: 25px; top: 272px; font-family: "Yellowtail", cursive; font-size: 34px; font-weight: 400; }
  .blurb { position: absolute; left: 26px; top: 346px; width: 390px; font-size: 7.8px; line-height: 9.1px; }
  .blurb p { margin-bottom: 9px; }
  .blurb-rule { position: absolute; left: 29px; top: 485px; width: 383px; height: 1px; background: rgba(255,255,255,.8); }
  .publisher-label { position: absolute; left: 27px; top: 544px; font-size: 7px; letter-spacing: 3.2px; text-transform: uppercase; }
  .publisher-info { position: absolute; left: 25px; top: 560px; width: 175px; font-size: 6.3px; line-height: 9.2px; }
  .isbn-box { position: absolute; left: 223px; top: 542px; width: 161px; height: 100px; background: #f8f8f8; }

  /* Spine */
  .spine { left: 581px; width: 42px; background: var(--spine-blue); }
  .spine-strip {
    position: absolute; left: -303px; top: 303px; width: 648px; height: 42px;
    transform: rotate(-90deg);
    display: flex; align-items: center; color: var(--white);
  }
  .spine-title { display: flex; align-items: center; margin-left: 22px; }
  .spine-title .caps { font-family: "Cinzel", serif; font-size: 18px; letter-spacing: 1px; }
  .spine-title .script { font-family: "Yellowtail", cursive; font-size: 30px; margin-left: 10px; }
  .spine-publisher { margin-left: auto; margin-right: 14px; font-size: 9px; letter-spacing: 3.6px; text-transform: uppercase; }

  /* Front cover */
  .front-cover { left: 651px; width: 432px; background: linear-gradient(200deg, #ffffff 55%, #f4f4f4 100%); text-align: center; }
  .front-author { position: absolute; top: 14px; width: 100%; font-size: 13.5px; color: var(--pink); }
  .front-title-caps { position: absolute; top: 48px; width: 100%; font-family: "Cinzel", serif; font-size: 21px; color: var(--teal); }
  .front-title-script { position: absolute; top: 68px; width: 100%; font-family: "Yellowtail", cursive; font-size: 84px; line-height: 1; color: var(--pink); }
  .front-art {
    position: absolute; left: 106px; top: 170px; width: 240px; height: 416px;
    border-radius: 120px 120px 40px 40px;
    background: linear-gradient(180deg, #1a8fa3 0%, #4f8aa6 45%, #c46a98 75%, #3f7890 100%);
  }
  .front-subtitle { position: absolute; top: 592px; width: 100%; font-size: 10px; font-weight: 500; line-height: 13px; color: var(--ink); text-transform: uppercase; letter-spacing: .6px; }
  .front-subtitle .accent { color: var(--pink); }
  .publisher-band { position: absolute; left: 0; bottom: 0; width: 100%; height: 20px; background: var(--teal); color: var(--white); font-size: 13px; line-height: 20px; letter-spacing: 5px; text-transform: uppercase; }
</style>
</head>
<body>
<div class="canvas">

  <section class="cover-panel back-cover">
    <div class="author-photo" role="img" aria-label="Portrait photograph of the author"></div>
    <div class="bio-rule"></div>
    <p class="author-bio">Dr. Margo Oslan Pardevy is a Doctor of Physical Therapy, Owner of The Open Door Wellness and The Lantern Gate Publishing House, a Holistic Life Transformation Coach, and International Bestselling Author. Decades of professional experience with patients, students, and clients makes her coaching effective, efficient, and easily integrated into your life. Her passion is to support the well-being and healing of your heart, mind, body, and soul as you learn to love your authentic self. Margo will empower you to become the author of your own life story as you discover unconsidered possibilities, remove barriers to success and unlock your full potential to live a creative life you love. Her own personal life journey prepared her to use her voice to amplify the voices of others to create even more impact in the world. You can find her enjoying living her best life as a mom of three divine masculine men in the making and expanding her own potential as a perfectly imperfect human being.</p>

    <h2 class="about-heading">About the Book</h2>
    <div class="blurb">
      <p>This book will offer the wisdom and philosophies of a variety of different coaches to allow future clients to get a taste of you and your style and prepare them to work with you!</p>
      <p>A coach does not fix you. Or heal you. They coach you - offer thoughts to ponder, guidance, techniques to try. All to help you plays and succeed at the game of life.</p>
      <p>Each coach has their own personality, training, experience, method and philosophy they bring to the table. The underlying purpose is to guide you through the quiet harvest, to become the person you desire and aspire to be. Different coaches for different folks, yet they all have their own unique wisdom and special sauce to share.</p>
      <p>This book is a collection of just that. A tasting of the wisdom and philosophies of a variety of different coaches for you to experience.</p>
    </div>
    <div class="blurb-rule"></div>

    <p class="publisher-label">The Lantern Gate Publishing House</p>
    <p class="publisher-info">Contrary to popular belief, Lorem Ipsum is not simply random text. It has roots in a piece of classical Latin literature from 45 BC, making it over 2000 years old. Elden Marrow, a Latin professor at Ashgrove College in Vermont, looked up one of the more obscure Latin words, consectetur, from a Lorem Ipsum passage, and going through the cites of the word in classical literature, discovered the undoubtable source.</p>
    <div class="isbn-box"></div>
  </section>

  <section class="cover-panel spine">
    <div class="spine-strip">
      <div class="spine-title">
        <span class="caps">The Quiet</span>
        <span class="script">Harvest</span>
      </div>
      <span class="spine-publisher">The Lantern Gate Publishing House</span>
    </div>
  </section>

  <section class="cover-panel front-cover">
    <p class="front-author">Dr. Marguerite Oslan Pardevy</p>
    <h1 class="front-title-caps">The Quiet</h1>
    <p class="front-title-script">Harvest</p>
    <div class="front-art" role="img" aria-label="Illustration of a human head silhouette formed from teal and pink butterflies"></div>
    <p class="front-subtitle">Field Notes <span class="accent">Gathered</span> By Many Guides<br>For Thriving On Every <span class="accent">Road Ahead</span></p>
    <div class="publisher-band">The Lantern Gate Publishing House</div>
  </section>

</div>
</body>
</html>
```